Suchen ansprechendes & seriöses Urkunden/Zertifikat Design für Webseite & Druck
Zielgruppe
Auf unserer Webseite http://rege-im-alter-netz.de können sich Unternehmen, Institutionen und Vereine ihre Seniorenfreundlichkeit durch ein Zertifikat bestätigen und zertifizieren lassen.
Unsere Kundengruppen: Hotel – Gastronomie – Wellness – Reisen und Touristik – Touristikregionen – Seniorenshop – Onlineshop – Unternehmen als Dienstleister – Medizin und Health-Service – Apotheke – Altenheim – Pflegeheim – Seniorenheim – Vereine – Seniorenservice – Zahnärzte – Fitnessstudio – Sportstudio – Physiotherapie – Sportverein – Golfclub – und viele weitere seniorenfreundliche Institutionen.
Aufgabenstellung
Auftrag- Ausschreibung:
- Erstellung eines Design:
- Urkunde für Webseite rege-im-alter-netz.de - Das Zertifikat "Rege im Alter“
Funktion:
Kunde erkennt das Zertifikat - Logo auf einer Webseite und Klickt auf dieses.
Er wird weitergeleitet auf eine Unterseite, worin die Richtlinien und die Urkunde sichtbar wird.
Zielgruppe:
- Unternehmen, welche das Zertifikat auf Ihre Webseite setzen. Die Urkunde gibt Auskunft, dass der Dienstleister einen besonderen Service für Senioren ausübt. Die Urkunde ist sichtbar auf der Webseite, indem das Logo angeklickt wird. Die Urkunde gibt es ebenfalls als Download, damit der Kunde diese in seinen Geschäftsräumen aufhängen kann oder diese in seinen Werbeunterlagen präsentieren kann.
- Verbraucher sollen beeindruckt sein, von der Urkunde, welches Vertrauen ausstrahlt, aber auch Seriosität
Folgende Ausstrahlung soll die Urkunde haben:
- Soll Mitbewerber des Zertifikatsinhaber beeindrucken und das Verlangen aufzeigen, sich ebenfalls zertifizieren zu lassen ( ca: 70% der Kunden sind Mitbewerber … ). Nach dem Motto "Das Logo ist super und edel, das muss ich auch haben!"
- Der Kunde als Verbraucher soll Vertrauen gewinnen, die Daten sollen gut sichtbar sein, aber nicht verkitscht wie eine Urkunde bei einer Kaffeefahrt. Der Verbraucher geht auf das Zertifikat und kommt zur Urkunde, deshalb soll die Farbe, und Darstellung, Seriosität des Unternehmens ausstrahlen.
Sonstiges
- Die Urkunde soll dem neuen Design unserer Seite (zu sehen unter: http://guetesiegel-welt.de) angepasst sein.
- Vor Auftragsendvergabe erhalten Sie noch ein telefonisches Briefing über unsere Erfahrungswerte
Link zur bestehenden alten Webseite (Altes Design): http://rege-im-alter-netz.de
Info Verbraucher: http://www.rege-im-alter-netz.de/verbraucher/
Info zum Zertifikat: http://www.rege-im-alter-ne..

```html
<!DOCTYPE html>
<html lang="de">
<head>
<meta charset="utf-8">
<title>Zertifikat – Rege im Alter</title>
<link rel="stylesheet" href="https://fonts.googleapis.com/css2?family=Raleway:wght@200;400;600;700&display=swap">
<style>
  :root{
    --paper-light:#f6f1e9;
    --paper-dark:#e6dccd;
    --frame:#b9a486;
    --frame-band:#cdbb9f;
    --title:#6e5c46;
    --accent:#7c5a30;
    --label:#8e6d42;
    --value:#2f2a25;
    --seal-ring:#c9c4be;
    --seal-core:#f2efea;
    --signature:#d8cdbd;
  }
  *{margin:0;padding:0;box-sizing:border-box}
  html,body{width:850px;height:1200px;overflow:hidden}
  body{font-family:"Raleway",sans-serif;background:var(--paper-light)}
  .certificate{
    position:relative;width:850px;height:1200px;overflow:hidden;
    background:radial-gradient(ellipse at 50% 40%,var(--paper-light) 0%,var(--paper-dark) 100%);
  }
  .frame{position:absolute;left:0;top:0}
  .heading{
    position:absolute;left:0;width:850px;text-align:center;top:112px;
    font-weight:200;font-size:112px;letter-spacing:4px;color:var(--title);line-height:1;
  }
  .subheading{
    position:absolute;left:0;width:850px;text-align:center;top:238px;
    font-weight:700;font-size:44px;color:var(--accent);line-height:1;
  }
  .details{position:absolute;left:0;top:0;width:850px;font-size:23px;line-height:28px}
  .row{position:absolute;left:0;display:flex}
  .label{width:316px;text-align:right;font-weight:600;color:var(--label);padding-right:10px}
  .value{color:var(--value);font-weight:400}
  .seal{position:absolute;left:480px;top:758px}
  .signatures{position:absolute;left:0;top:0}
  .signature{position:absolute;border-radius:40% 60% 50% 50%;background:var(--signature);opacity:.55}
  .signer{position:absolute;font-size:17px;color:var(--value)}
  .confirmed{position:absolute;left:156px;top:1005px;font-weight:600;font-size:23px;color:var(--label)}
  .page-number{position:absolute;left:14px;top:1172px;font-weight:700;font-size:22px;color:var(--accent)}
</style>
</head>
<body>
<main class="certificate">
  <svg class="frame" width="850" height="1200" viewBox="0 0 850 1200" aria-hidden="true">
    <rect x="68" y="58" width="714" height="1070" fill="none" stroke="var(--frame)" stroke-width="1.5"/>
    <rect x="80" y="70" width="690" height="1046" fill="none" stroke="var(--frame)" stroke-width="1"/>
    <rect x="200" y="60" width="450" height="8" fill="var(--frame-band)"/>
    <rect x="200" y="1118" width="450" height="8" fill="var(--frame-band)"/>
    <rect x="70" y="330" width="8" height="560" fill="var(--frame-band)"/>
    <rect x="772" y="330" width="8" height="560" fill="var(--frame-band)"/>
    <line x1="395" y1="64" x2="455" y2="64" stroke="var(--accent)" stroke-width="3"/>
  </svg>

  <h1 class="heading">ZERTIFIKAT</h1>
  <h2 class="subheading">REGE IM ALTER</h2>

  <section class="details">
    <div class="row" style="top:358px"><span class="label">Zertifikat ID:</span><span class="value">7250441e9e</span></div>
    <div class="row" style="top:418px"><span class="label">Anbieter:</span><span class="value">Rege im Alter<br>Ihr Zertifizierungsdienst</span></div>
    <div class="row" style="top:500px"><span class="label">Status:</span><span class="value">aktiv</span></div>
    <div class="row" style="top:560px"><span class="label">Unternehmen:</span><span class="value">Senioren Service Linde<br>Birkenweg 8<br>54321 Musterort<br>Deutschland<br>kontakt@linde-service.org</span></div>
    <div class="row" style="top:762px"><span class="label">Vertretungs-<br>berechtigter:</span><span class="value">Frau Helga<br>Linde</span></div>
    <div class="row" style="top:824px"><span class="label">Erstprüfung am:</span><span class="value">07.04.2017</span></div>
    <div class="row" style="top:872px"><span class="label">gültig bis:</span><span class="value">07.04.2019</span></div>
  </section>

  <svg class="seal" width="200" height="200" viewBox="0 0 200 200" role="img" aria-label="Prüfsiegel">
    <circle cx="100" cy="97" r="92" fill="var(--seal-ring)"/>
    <circle cx="100" cy="97" r="66" fill="var(--seal-core)"/>
  </svg>

  <div class="signatures">
    <div class="signature" role="img" aria-label="Unterschrift K. Brandt" style="left:295px;top:950px;width:145px;height:62px"></div>
    <div class="signature" role="img" aria-label="Unterschrift M. Vogel" style="left:455px;top:945px;width:135px;height:65px"></div>
    <span class="signer" style="left:332px;top:1014px">K. Brandt</span>
    <span class="signer" style="left:465px;top:1012px">M. Vogel</span>
  </div>
  <p class="confirmed">Bestätigt von:</p>

  <span class="page-number">27</span>
</main>
</body>
</html>
```